VALMIK GROUP

This is a company that provides executive protection. Our motto is "New Era in Protection"... I don't want this to look like other security websites. I want it to be clean and sharp and represent a new era. We are based in the bay area so maybe a picture of San Francisco in the background?
I want it to be able to funnel down a couple different categories.
1. About Us
2. Services (Executive Protection, Covert Protection, Residential Protection & Intelligence)
3. Blue Pike (Training & Consulting)
4. Contact Us
I want it to be very clean and modern. I don't want there to be any pictures of bodyguards with ear pieces like every other website.
Target Market(s)
Ultra High Net Worth Individuals
Coding
Coded - Design and coding required
Number of Pages Required
1 page
Requirements
Must have
- Colors of my Symbol
Nice to have
- City in the background, San Francisco, New York or the Thornmeadow Club in Montana.
Should not have
- Should not look like an KVM website or have photos of bodyguards. I want this to be a clean and simple website with my logo

```html
<!DOCTYPE html>
<html lang="en">
<head>
<meta charset="utf-8">
<title>VALMIK GROUP — New Era in Protection</title>
<link href="https://fonts.googleapis.com/css2?family=Roboto:wght@300;400;500;700&display=swap" rel="stylesheet">
<style>
:root{
  --red:#8b1a1d;
  --red-dark:#6f1215;
  --ink:#111;
  --text:#333;
  --grey-bg:#f1f1f1;
  --pin-grey:#a9a9a9;
  --navy:#0e2472;
  --white:#fff;
}
*{box-sizing:border-box;margin:0;padding:0}
html,body{width:1200px;height:3369px;overflow:hidden}
body{position:relative;font-family:'Roboto',sans-serif;color:var(--text);background:var(--white)}
.abs{position:absolute}
a{color:inherit;text-decoration:none}

/* header */
.topline{top:34px;font-size:13px;color:#333}
.topline svg{vertical-align:-2px;margin-right:6px}
.nav{top:92px;font-size:13px;font-weight:500;color:#222;display:flex;gap:34px;align-items:center}
.nav .active{background:var(--red);color:#fff;border-radius:16px;padding:8px 17px}
.nav .login{color:var(--red)}
.brand{left:0;width:1200px;top:86px;text-align:center;color:var(--ink);font-weight:700;line-height:1}
.brand .name{font-size:34px;letter-spacing:2px}
.brand .sub{font-size:13px;letter-spacing:9px;margin-top:4px}

/* hero */
.hero{top:149px;left:0;width:1200px;height:672px}
.hero-box{left:248px;top:503px;width:704px;height:200px;background:rgba(70,70,70,.75);text-align:center;color:#fff;padding-top:22px}
.hero-box h1{font-size:42px;font-weight:500;letter-spacing:.5px}
.hero-box p{font-size:21px;font-weight:300;line-height:32px;margin-top:10px;padding:0 20px}
.dots{top:777px;left:0;width:1200px;display:flex;justify-content:center;gap:14px}
.dots span{width:12px;height:12px;border-radius:50%;background:#111}
.dots span.on{background:#fff}

/* sections */
.section-title{left:0;width:1200px;text-align:center;font-size:42px;font-weight:300;color:var(--ink);line-height:1}
.section-title b{font-weight:500}
.section-title:after{content:"";display:block;width:158px;height:4px;background:var(--ink);margin:10px auto 0}
.lead{left:0;width:1200px;text-align:center;font-size:13.5px;line-height:22px;color:#333}
.btn{background:var(--red);color:#fff;font-size:16px;font-weight:500;border-radius:14px;display:flex;align-items:center;justify-content:center;height:55px;width:170px}

.services-bg{top:1213px;left:0;width:1200px;height:621px;background:var(--grey-bg)}
.service{width:240px;text-align:center}
.service h3{font-size:17px;font-weight:500;color:var(--ink);margin-top:34px}
.service.featured h3{color:var(--red)}
.service p{font-size:12.5px;line-height:21px;margin-top:12px;color:#333;padding:0 10px}

.photo{border:5px solid #fff;box-shadow:0 0 6px rgba(0,0,0,.35);border-radius:12px}
.card-title{font-size:20px;font-weight:500;color:var(--ink);text-align:center}
.card-text{font-size:13.5px;line-height:22px;text-align:center}

/* contact */
.contact{top:2624px;left:0;width:1200px;height:454px}
.contact-brand{left:130px;top:2770px;width:242px;color:#fff;text-align:center;font-weight:700;line-height:1}
.contact-brand .name{font-size:48px;letter-spacing:3px}
.contact-brand .sub{font-size:20px;letter-spacing:14px;margin-top:10px}
.contact h2{font-size:34px;font-weight:300;color:#fff}
.field{border-bottom:1px solid rgba(255,255,255,.7);color:rgba(255,255,255,.85);font-size:13px;font-weight:300;padding-bottom:6px}
.send{background:var(--navy);color:#fff;font-size:20px;font-weight:300;display:flex;align-items:center;justify-content:center}

/* footer */
.foot-h{top:3130px;font-size:21px;font-weight:500;color:var(--ink)}
.foot-list{top:3177px;font-size:13px;line-height:25.5px;color:#111}
.news-note{top:3166px;left:663px;font-size:12px;font-weight:500;color:#111}
.news-input{top:3196px;left:663px;width:275px;height:43px;border:1px solid #333;font-size:13px;color:#111;display:flex;align-items:center;padding-left:10px}
.news-btn{top:3196px;left:937px;width:112px;height:43px;background:#000;color:#fff;font-size:12px;font-weight:700;display:flex;align-items:center;justify-content:center}
.social{top:3258px;left:664px;display:flex;gap:8px}
.social span{width:40px;height:40px;border:2px solid #444;border-radius:50%}
.copy{top:3329px;left:0;width:1200px;text-align:center;font-size:12.5px;font-weight:500;color:#222}
.bottom-bar{top:3359px;left:0;width:1200px;height:10px;background:#333}
</style>
</head>
<body>

<!-- header -->
<div class="abs topline" style="left:111px"><svg width="11" height="11" viewBox="0 0 24 24"><path fill="#333" d="M6.6 10.8a15 15 0 006.6 6.6l2.2-2.2c.3-.3.7-.4 1-.2 1.1.4 2.3.6 3.6.6.6 0 1 .4 1 1V20c0 .6-.4 1-1 1A17 17 0 013 4c0-.6.4-1 1-1h3.5c.6 0 1 .4 1 1 0 1.3.2 2.5.6 3.6.1.3 0 .7-.2 1z"/></svg>+1-800-55501234</div>
<div class="abs topline" style="left:904px"><svg width="12" height="10" viewBox="0 0 24 18"><path fill="#333" d="M0 0h24v18H0zM2 2l10 7 10-7"/></svg>support@valmikgroup.com</div>

<nav class="abs nav" style="left:111px"><a class="active">HOME</a><a>ABOUT US</a><a>SERVICES ▾</a></nav>
<nav class="abs nav" style="left:800px;top:100px"><a>BLUE PIKE ▾</a><a>CONTACT US</a><a class="login">&#9679; LOGIN</a></nav>

<div class="abs brand" style="top:88px"><div class="name">VALMIK</div><div class="sub">GROUP</div></div>

<!-- hero -->
<svg class="abs hero" viewBox="0 0 1200 672" role="img" aria-label="San Francisco bay bridge at sunset with city skyline">
  <defs>
    <linearGradient id="sky" x1="0" y1="0" x2="0" y2="1">
      <stop offset="0" stop-color="#1e2f6e"/>
      <stop offset=".45" stop-color="#6b4f86"/>
      <stop offset=".75" stop-color="#d0865a"/>
      <stop offset="1" stop-color="#8a6a58"/>
    </linearGradient>
    <radialGradient id="sun" cx=".58" cy=".5" r=".35">
      <stop offset="0" stop-color="#ffd08a" stop-opacity=".9"/>
      <stop offset="1" stop-color="#ffd08a" stop-opacity="0"/>
    </radialGradient>
  </defs>
  <path d="M0 0H1200V513L600 672L0 513Z" fill="url(#sky)"/>
  <path d="M0 0H1200V513L600 672L0 513Z" fill="url(#sun)"/>
</svg>
<div class="abs hero-box">
  <h1>NEW ERA IN PROTECTION</h1>
  <p>There are many variations of passages of Lorem Ipsum available, but the majority have suffered alteration in some form, by injected humour, or randomised words which don't look even slightly.</p>
</div>
<div class="abs dots"><span></span><span class="on"></span><span></span><span></span></div>

<!-- welcome -->
<h2 class="abs section-title" style="top:898px"><b>WELCOME</b> TO VALMIK</h2>
<p class="abs lead" style="top:970px;left:225px;width:750px">There are many variations of passages of Lorem Ipsum available, but the majority have suffered alteration in some form, by injected humour, or randomised words which don't look even slightly believable. If you are going to use a passage of Lorem Ipsum, you need to be sure there isn't anything embarrassing hidden in the middle of text. All the Lorem Ipsum generators on the Internet tend to repeat predefined chunks as necessary,</p>
<a class="abs btn" style="left:515px;top:1086px">BLUE PIKE NOW !</a>

<!-- services -->
<div class="abs services-bg"></div>
<h2 class="abs section-title" style="top:1268px"><b>OUR</b> SERVICES</h2>
<p class="abs lead" style="top:1338px;left:225px;width:750px">There are many variations of passages of Lorem Ipsum available, but the majority have suffered alteration in some form, by injected humour, or randomised words which don't look even slightly believable. If you are going</p>

<svg class="abs" style="left:0;top:1422px" width="1200" height="240" viewBox="0 0 1200 240">
  <defs>
    <g id="pin-shield"><path d="M0 -24L20 -16V2C20 14 10 22 0 26C-10 22-20 14-20 2V-16Z" fill="#555"/></g>
  </defs>
  <g transform="translate(220 104)">
    <path d="M-103 0A103 103 0 1 1 -103 0.1Z" fill="var(--pin-grey)"/>
    <circle r="103" fill="#a9a9a9"/><path d="M-22 95L0 132L22 95Z" fill="#a9a9a9"/>
    <circle r="74" fill="#fff"/><use href="#pin-shield"/>
  </g>
  <g transform="translate(474 104)">
    <circle r="103" fill="#8b1a1d"/><path d="M-22 95L0 132L22 95Z" fill="#8b1a1d"/>
    <circle r="74" fill="#fff"/><path d="M0 -24L20 -16V2C20 14 10 22 0 26C-10 22-20 14-20 2V-16Z" fill="#8b1a1d"/>
  </g>
  <g transform="translate(729 104)">
    <circle r="103" fill="#a9a9a9"/><path d="M-22 95L0 132L22 95Z" fill="#a9a9a9"/>
    <circle r="74" fill="#fff"/><rect x="-22" y="-22" width="44" height="44" rx="4" fill="#555"/>
  </g>
  <g transform="translate(986 104)">
    <circle r="103" fill="#a9a9a9"/><path d="M-22 95L0 132L22 95Z" fill="#a9a9a9"/>
    <circle r="74" fill="#fff"/><use href="#pin-shield"/>
  </g>
</svg>

<div class="abs service" style="left:100px;top:1653px"><h3>EXECUTIVE PROTECTION</h3><p>There are many variations passages of Lorem Ipsum available, but have suffered alteration</p></div>
<div class="abs service featured" style="left:354px;top:1653px"><h3>COVERT PROTECTION</h3><p>There are many variations passages of Lorem Ipsum available, but have suffered alteration</p></div>
<div class="abs service" style="left:609px;top:1653px"><h3>RESIDENTIAL PROTECTION</h3><p>There are many variations passages of Lorem Ipsum available, but have suffered alteration</p></div>
<div class="abs service" style="left:866px;top:1653px"><h3>INTELLIGENCE</h3><p>There are many variations passages of Lorem Ipsum available, but have suffered alteration</p></div>

<!-- blue pike -->
<h2 class="abs section-title" style="top:1877px"><b>OUR</b> BLUE PIKE</h2>
<p class="abs lead" style="top:1950px;left:225px;width:750px">There are many variations of passages of Lorem Ipsum available, but the majority have suffered alteration in some form, by injected humour, or randomised words which don't look even slightly believable. If you are going</p>

<div class="abs photo" role="img" aria-label="Security staff member in a crowd" style="left:108px;top:2036px;width:458px;height:310px;background:linear-gradient(100deg,#1d1d22 0%,#2b2b33 45%,#7f7a84 70%,#b9b2b0 100%)"></div>
<div class="abs photo" role="img" aria-label="Consultants meeting in a glass office" style="left:627px;top:2036px;width:461px;height:310px;background:linear-gradient(180deg,#9fb2c8 0%,#c3ccd6 45%,#2f3440 75%,#5b4636 100%)"></div>

<div class="abs card-title" style="left:108px;width:458px;top:2377px">TRAINING</div>
<p class="abs card-text" style="left:128px;width:418px;top:2421px">There are many variations of passages of Lorem Ipsum available, but the majority have suffered alteration in some form, by injected humour, or randomised words which</p>
<a class="abs btn" style="left:252px;top:2513px">BLUE PIKE NOW !</a>

<div class="abs card-title" style="left:627px;width:461px;top:2377px">CONSULTING</div>
<p class="abs card-text" style="left:648px;width:418px;top:2421px">There are many variations of passages of Lorem Ipsum available, but the majority have suffered alteration in some form, by injected humour, or randomised words which</p>
<a class="abs btn" style="left:772px;top:2513px">BLUE PIKE NOW !</a>

<!-- contact -->
<svg class="abs contact" viewBox="0 0 1200 454" aria-hidden="true"><path d="M0 0H1200V369L600 454L0 369Z" fill="#8b1a1d"/></svg>
<div class="abs contact-brand"><div class="name">VALMIK</div><div class="sub">GROUP</div></div>
<h2 class="abs" style="top:2670px;left:464px;width:550px;text-align:center;font-size:34px;font-weight:300;color:#fff">Get in touch with us</h2>
<div class="abs field" style="left:464px;top:2756px;width:251px">* Your Name</div>
<div class="abs field" style="left:763px;top:2756px;width:251px">* Your e-mail</div>
<div class="abs field" style="left:464px;top:2817px;width:550px">* Your Message</div>
<a class="abs send" style="left:652px;top:2890px;width:166px;height:55px">Get in touch</a>

<!-- footer -->
<h3 class="abs foot-h" style="left:146px">Company</h3>
<div class="abs foot-list" style="left:147px">San Francisco,<br>New York<br>simply dummy text<br>Tel .: +1 234 -50172<br>E-mail: info@valmikgroup.com</div>
<h3 class="abs foot-h" style="left:465px">Quick ling</h3>
<div class="abs foot-list" style="left:466px">Home<br>About Us<br>Services<br>Blue Pike<br>Contact Us</div>
<h3 class="abs foot-h" style="left:663px">NewsLatter</h3>
<div class="abs news-note">Entice shoppers to sign up for your list</div>
<div class="abs news-input">Your Email</div>
<div class="abs news-btn">SUBSCRIBE</div>
<div class="abs social"><span></span><span></span><span></span><span></span><span></span></div>
<div class="abs copy">© 2021 valmikgroup. All rights reserved</div>
<div class="abs bottom-bar"></div>

</body>
</html>
```